Product label design needed for an odor removal line of products.

I need a label designed for an odor removal product line. There are eight additional odor removal products that I will need labels designed for so the winner will have additional work from me. I would like each of those products to have a similar look and feel in each one. This contest is for one of the products. The Breezeward Pod 385 (would love a better name if you are so inclined -many people know what it is by the 385). The no smell formula does not mask odors, it eliminates odors at their source . Also Reduces Allergens! Simply open silver packet and place in dispenser. Great for use in cars, near pet beds or litter boxes, near diaper pails -anywhere odors are a problem. Lasts 60-90 days. Safe to use. Other uses: Nursing homes, hotel rooms, locker rooms, teenage boy rooms, basements... Eco Friendly! No VOC's or phthalates! Do not consume. Keep out of reach of children and pets. Replace every 60-90 days. I put the picture of my logo , the product as it is packaged and a picture of the actual product and the dispenser it will go in. the package is 4x5 in silver packet with .25 seam on the side and .5 seam on the top and bottom. (Dispenser will have a label with reorder information on it. to be designed later) You do not have to put all information provided on the label. It is to be used as you see fit. I tend to like clean, bold designs but am open to all options. Prefer not to use word air freshener.

Target Market(s)

Men and women between 30-65

Industry/Entity Type

Cleaning Product

Font styles to use
Sans Serif

Colors
acd136
9bcb3c
ffffff

Requirements
Must have
• ability for concept/look to be used for a laundry product, smaller odor elimination pouch, odor removing canister and spray as well
Nice to have
• I like greens but am open to designers to decide
Should not have
• word air freshener

```html
<!DOCTYPE html>
<html lang="en">
<head>
<meta charset="utf-8">
<title>The Breezeward Pod 385 – Label</title>
<link href="https://fonts.googleapis.com/css2?family=Roboto:wght@700;900&family=Roboto+Condensed:wght@700&display=swap" rel="stylesheet">
<style>
  :root {
    --bg-light: #f7f7f1;
    --bg-warm: #eceee2;
    --panel: #f2f2f2;
    --ink: #151515;
    --green: #9bcb3c;
    --lime: #acd136;
    --leaf-dark: #3f9a2a;
    --leaf-mid: #6cbf3a;
    --icon-green: #2f9a37;
    --white: #ffffff;
  }
  * { margin: 0; padding: 0; box-sizing: border-box; }
  html, body { width: 857px; height: 1200px; overflow: hidden; }
  body { background: var(--white); font-family: "Roboto", Arial, sans-serif; }

  .label {
    position: relative;
    width: 857px;
    height: 1200px;
    overflow: hidden;
    background: radial-gradient(ellipse at 50% 45%, var(--bg-light) 0%, var(--bg-light) 45%, var(--bg-warm) 100%);
  }

  .foliage { position: absolute; border-radius: 50%; }
  .foliage--top-left {
    left: -70px; top: -60px; width: 250px; height: 340px;
    background: radial-gradient(ellipse at 40% 40%, var(--leaf-mid), var(--leaf-dark) 65%, rgba(63,154,42,0) 72%);
  }
  .foliage--bottom-right {
    left: 320px; top: 960px; width: 620px; height: 360px;
    border-radius: 50% 50% 0 0;
    background: radial-gradient(ellipse at 55% 60%, var(--leaf-mid), var(--leaf-dark) 60%, rgba(63,154,42,0) 72%);
  }

  .brand-badge {
    position: absolute;
    left: 610px; top: 36px;
    width: 188px; height: 188px;
    border-radius: 50%;
    background: var(--white);
    border: 6px solid var(--icon-green);
    display: flex; align-items: center; justify-content: center;
    text-align: center;
  }
  .brand-badge__name {
    font-weight: 700;
    font-size: 25px;
    line-height: 1.15;
    letter-spacing: 2px;
    color: var(--icon-green);
  }

  .title-panel {
    position: absolute;
    left: 321px; top: 333px;
    width: 476px; height: 345px;
    background: var(--panel);
  }
  .title-leaves {
    position: absolute;
    left: 450px; top: 357px;
    width: 340px; height: 310px;
    border-radius: 60% 40% 55% 45%;
    background: radial-gradient(ellipse at 55% 45%, var(--lime), var(--green) 55%, rgba(155,203,60,0) 72%);
  }
  .product-name {
    position: absolute;
    left: 106px; top: 447px;
    font-weight: 900;
    font-size: 48px;
    line-height: 1.45;
    color: var(--ink);
    white-space: nowrap;
  }
  .product-number {
    position: absolute;
    left: 472px; top: 431px;
    font-family: "Roboto Condensed", "Arial Narrow", sans-serif;
    font-weight: 700;
    font-size: 200px;
    line-height: 1;
    letter-spacing: -6px;
    color: var(--ink);
  }
  .title-rule {
    position: absolute;
    left: 60px; top: 631px;
    width: 697px; height: 14px;
    background: var(--green);
  }

  .claims {
    position: absolute;
    left: 0; top: 738px;
    width: 857px;
    list-style: none;
  }
  .claim { position: absolute; width: 260px; text-align: center; }
  .claim:nth-child(1) { left: 7px; }
  .claim:nth-child(2) { left: 292px; }
  .claim:nth-child(3) { left: 572px; }
  .claim__icon { display: block; width: 130px; height: 130px; margin: 0 auto; }
  .claim__text {
    display: block;
    margin-top: 16px;
    font-weight: 700;
    font-size: 19px;
    color: var(--ink);
  }
</style>
</head>
<body>
<main class="label">
  <div class="foliage foliage--top-left" role="img" aria-label="Cluster of fresh green leaves"></div>

  <div class="brand-badge">
    <span class="brand-badge__name">VERDANT<br>HAVEN</span>
  </div>

  <div class="title-panel"></div>
  <div class="title-leaves" role="img" aria-label="Bright green leaves behind the product number"></div>

  <h1 class="product-name">The Breezeward<br>Pod</h1>
  <div class="product-number">385</div>
  <div class="title-rule"></div>

  <ul class="claims">
    <li class="claim">
      <svg class="claim__icon" viewBox="0 0 132 132" aria-hidden="true">
        <circle cx="66" cy="66" r="61" fill="none" stroke="var(--icon-green)" stroke-width="6"/>
        <path d="M64 92 C40 90 34 62 40 46 C58 50 68 68 64 92 Z" fill="none" stroke="#1c1c1c" stroke-width="5" stroke-linejoin="round"/>
        <path d="M68 92 C92 90 98 62 92 46 C74 50 64 68 68 92 Z" fill="none" stroke="#1c1c1c" stroke-width="5" stroke-linejoin="round"/>
      </svg>
      <span class="claim__text">100 % NATURAL</span>
    </li>
    <li class="claim">
      <svg class="claim__icon" viewBox="0 0 132 132" aria-hidden="true">
        <circle cx="66" cy="66" r="61" fill="none" stroke="var(--icon-green)" stroke-width="6"/>
        <path d="M66 84 V56" stroke="#1c1c1c" stroke-width="5" stroke-linecap="round"/>
        <path d="M66 60 C64 46 54 40 44 42 C46 54 56 60 66 60 Z" fill="#1c1c1c"/>
        <path d="M66 56 C68 42 78 36 88 38 C86 50 76 56 66 56 Z" fill="#1c1c1c"/>
        <path d="M36 94 C48 82 84 82 96 94" fill="none" stroke="#1c1c1c" stroke-width="5" stroke-linecap="round"/>
      </svg>
      <span class="claim__text">NON-TOXIC</span>
    </li>
    <li class="claim">
      <svg class="claim__icon" viewBox="0 0 132 132" aria-hidden="true">
        <circle cx="66" cy="66" r="61" fill="none" stroke="var(--icon-green)" stroke-width="6"/>
        <path d="M56 36 H76 M60 36 V58 L42 92 H90 L72 58 V36" fill="none" stroke="#1c1c1c" stroke-width="5" stroke-linejoin="round"/>
        <circle cx="62" cy="80" r="5" fill="#1c1c1c"/>
        <circle cx="74" cy="84" r="4" fill="#1c1c1c"/>
        <line x1="26" y1="26" x2="106" y2="106" stroke="var(--icon-green)" stroke-width="6"/>
      </svg>
      <span class="claim__text">CHEMICAL-FREE</span>
    </li>
  </ul>

  <div class="foliage foliage--bottom-right" role="img" aria-label="Large green leaves rising from the bottom edge"></div>
</main>
</body>
</html>
```